KDR Business Card

Keystone Draper Resources is a successful and reputable financial services company.Our main services are home loans, commercial loans, vehicle finance and equipment finance. We also do development finance for property developers. Our company is always evolving to always be an industry leader in best financial service practices with access to the largest range of lenders in the country.

We want the business card to reflect our national finance company. Modern, professional corporate image. At the same time the concept of Keystone Draper Resources is that we help build wealth for you but the process for the client is an enjoyable peaceful experience. Not stressful at all .....

Colors to be same as the logo .... gold silver black white as the options

On the reverse side of the card I wanted either just the logo symbol or the logo symbol and text of the logo ....

It could be on a black background ..... or silver or gold .... want it to be quite striking to look at when you first see the card.

On the other side of the card I wanted the following details:

Martin Haldane
Director

0438 927 604

martin@kdrgrp.com.au

Po Box 718
Ferndale ACT 2614

www.kdrgrp.com.au

ACN 618 204 957 (This can be in very small print and can be in the bottom corner of the card or somewhere not very prominent)

As requested Ive uploaded the logo file in both .ai and .pdf formats. Please let me know if you need anything else. Thanks

Reason: Still deciding on which design I like best. I will provide individual feedback as well.

```html
<!DOCTYPE html>
<html lang="en">
<head>
<meta charset="utf-8">
<title>KDR Business Card</title>
<link rel="stylesheet" href="https://fonts.googleapis.com/css2?family=Cinzel:wght@500&family=Tinos&display=swap">
<style>
  :root {
    --stage: #e9e6e1;
    --card-black: #0c0c0d;
    --card-glow: #3a3a3c;
    --gold: #e9c54a;
    --gold-soft: #c9a545;
    --bronze-dim: #3a2516;
    --white: #f4f4f4;
    --silver: #d9d9d9;
  }
  * { margin: 0; padding: 0; box-sizing: border-box; }
  html, body { width: 1200px; height: 900px; overflow: hidden; }
  body {
    background: var(--stage);
    display: flex;
    align-items: center;
    justify-content: center;
    gap: 40px;
    font-family: "Tinos", "Times New Roman", serif;
  }
  .card {
    position: relative;
    width: 540px;
    height: 330px;
    border-radius: 2px;
    background: radial-gradient(ellipse at 45% 30%, var(--card-glow) 0%, #1a1a1b 45%, var(--card-black) 100%);
    box-shadow: 0 10px 24px rgba(0,0,0,0.28);
    overflow: hidden;
  }
  /* front: brand side */
  .card-front .brand {
    position: absolute;
    left: 50%; top: 50%;
    transform: translate(-50%, -50%);
    display: flex;
    align-items: center;
    gap: 16px;
    white-space: nowrap;
  }
  .card-front .brand-dot {
    width: 84px; height: 84px;
    border-radius: 50%;
    background: var(--bronze-dim);
  }
  .card-front .brand-name {
    font-size: 30px;
    color: var(--bronze-dim);
  }
  /* back: details side */
  .card-back .brand {
    position: absolute;
    left: 34px; top: 36px;
    display: flex;
    align-items: center;
    gap: 10px;
  }
  .card-back .brand-dot {
    width: 44px; height: 44px;
    border-radius: 50%;
    background: var(--silver);
  }
  .card-back .brand-name {
    font-size: 19px;
    color: var(--gold-soft);
    white-space: nowrap;
  }
  .person {
    position: absolute;
    left: 300px; top: 112px;
    font-family: "Cinzel", "Times New Roman", serif;
    color: var(--gold);
    line-height: 1.2;
  }
  .person .role { font-size: 19px; letter-spacing: 1px; }
  .person .name { font-size: 22px; letter-spacing: 1px; }
  .person-icon { position: absolute; left: 256px; top: 118px; }
  .contact-list {
    position: absolute;
    left: 198px; top: 188px;
    list-style: none;
    color: var(--white);
    font-size: 15px;
    line-height: 1.3;
  }
  .contact-list li {
    display: grid;
    grid-template-columns: 28px auto;
    column-gap: 12px;
    align-items: start;
    margin-bottom: 6px;
  }
  .contact-list svg { width: 22px; height: 20px; fill: var(--white); }
  .company-number {
    position: absolute;
    right: 22px; bottom: 16px;
    font-size: 10px;
    color: var(--white);
    letter-spacing: 0.3px;
  }
</style>
</head>
<body>

  <section class="card card-front" aria-label="Card front">
    <div class="brand">
      <span class="brand-dot"></span>
      <span class="brand-name">Keystone Draper Resources</span>
    </div>
  </section>

  <section class="card card-back" aria-label="Card back">
    <div class="brand">
      <span class="brand-dot"></span>
      <span class="brand-name">Keystone Draper Resources</span>
    </div>

    <svg class="person-icon" width="30" height="32" viewBox="0 0 30 32" aria-hidden="true">
      <circle cx="15" cy="9" r="7" fill="var(--white)"/>
      <path d="M2 31 C2 21 8 18 15 18 C22 18 28 21 28 31 Z" fill="var(--white)"/>
    </svg>
    <div class="person">
      <div class="role">Director</div>
      <div class="name">Martin Haldane</div>
    </div>

    <ul class="contact-list">
      <li>
        <svg viewBox="0 0 22 20" aria-hidden="true"><path d="M2 6 C2 2 20 2 20 6 L17 8 L14 6 L8 6 L5 8 Z"/><rect x="5" y="9" width="12" height="9" rx="2"/><circle cx="11" cy="13.5" r="2.5" fill="#111"/></svg>
        <span>0438 927 604</span>
      </li>
      <li>
        <svg viewBox="0 0 22 20" aria-hidden="true"><rect x="1" y="3" width="20" height="14" rx="1.5"/><path d="M2 4 L11 11 L20 4" stroke="#111" stroke-width="1.6" fill="none"/></svg>
        <span>martin@kdrgrp.com.au</span>
      </li>
      <li>
        <svg viewBox="0 0 22 20" aria-hidden="true"><rect x="1" y="1" width="20" height="13" rx="1.5"/><rect x="8" y="14" width="6" height="3"/><rect x="5" y="17" width="12" height="2"/></svg>
        <span>www.kdrgrp.com.au</span>
      </li>
      <li>
        <svg viewBox="0 0 22 20" aria-hidden="true"><path d="M11 19 C6 13 4 10 4 7.5 A7 7 0 0 1 18 7.5 C18 10 16 13 11 19 Z"/><circle cx="11" cy="7.5" r="2.5" fill="#111"/></svg>
        <span>Po Box 718<br>Ferndale ACT 2614</span>
      </li>
    </ul>

    <p class="company-number">ACN 618 204 957</p>
  </section>

</body>
</html>
```